BRTW Traditional Business Card Project

Please see attached....just a simple business card... on attachment- please use the exact font, style, etc as the attached "Dal Rupert Huxley" card... however, replace with the "Owen Bartholomew Lindqvist" text and address below the card.

```html
<!DOCTYPE html>
<html lang="en">
<head>
<meta charset="utf-8">
<title>BRTW Business Card – Owen Bartholomew Lindqvist</title>
<link rel="stylesheet" href="https://fonts.googleapis.com/css2?family=Tinos:wght@400;700&family=Questrial&display=swap">
<style>
  :root {
    --backdrop: #5c5c5c;
    --card: #ffffff;
    --ink: #1c1c1c;
    --ink-soft: #4a4a4a;
    --rule: #6a6a6a;
  }
  html, body {
    margin: 0;
    width: 1200px;
    height: 1200px;
    overflow: hidden;
    background: var(--backdrop);
  }
  .card {
    position: absolute;
    left: 80px;
    top: 303px;
    width: 1040px;
    height: 594px;
    background: var(--card);
    color: var(--ink);
  }
  .firm {
    position: absolute;
    left: 49px;
    top: 66px;
    width: 484px;
    text-align: center;
    font-family: "Tinos", "Times New Roman", serif;
  }
  .firm-name {
    font-size: 40px;
    line-height: 1;
    font-variant: small-caps;
    letter-spacing: 0.5px;
    white-space: nowrap;
  }
  .firm-suffix {
    margin-top: 6px;
    font-size: 17px;
    font-weight: 700;
    color: var(--ink-soft);
    letter-spacing: 0.6px;
  }
  .person {
    position: absolute;
    left: 599px;
    top: 64px;
  }
  .person-name {
    font-family: "Tinos", "Times New Roman", serif;
    font-weight: 700;
    font-size: 20px;
    letter-spacing: 0.8px;
    line-height: 1;
    white-space: nowrap;
  }
  .person-title {
    margin-top: 22px;
    font-family: "Questrial", "Helvetica Neue", sans-serif;
    font-size: 23px;
    letter-spacing: 0.6px;
    color: var(--ink-soft);
    line-height: 1;
    padding-bottom: 13px;
    border-bottom: 2px solid var(--rule);
    width: 249px;
  }
  .contact {
    position: absolute;
    left: 599px;
    top: 396px;
    margin: 0;
    padding: 0;
    list-style: none;
    font-family: "Questrial", "Helvetica Neue", sans-serif;
    color: var(--ink-soft);
  }
  .contact li {
    display: flex;
    align-items: center;
    height: 40px;
    font-size: 21px;
    letter-spacing: 1.4px;
  }
  .contact .small-caps {
    font-size: 18px;
    letter-spacing: 1.6px;
    font-variant: small-caps;
    text-transform: lowercase;
  }
  .contact svg {
    width: 24px;
    height: 24px;
    margin-right: 15px;
    flex: none;
  }
  .address {
    position: absolute;
    left: 49px;
    top: 483px;
    font-family: "Questrial", "Helvetica Neue", sans-serif;
    font-size: 21px;
    letter-spacing: 1.4px;
    line-height: 36px;
    color: var(--ink-soft);
    text-transform: uppercase;
  }
</style>
</head>
<body>
  <div class="card">
    <div class="firm">
      <div class="firm-name">Bay Region Trial Works</div>
      <div class="firm-suffix">TRIAL WORKS, PLC</div>
    </div>

    <div class="person">
      <div class="person-name">OWEN BARTHOLOMEW LINDQVIST</div>
      <div class="person-title">ATTORNEY AT LAW</div>
    </div>

    <ul class="contact">
      <li>
        <svg viewBox="0 0 24 24" aria-hidden="true"><circle cx="12" cy="12" r="12" fill="#1c1c1c"/><path d="M8.2 6.5l2 2.2-1.1 1.5c.8 1.7 2 2.9 3.7 3.8l1.5-1.1 2.2 2-1.2 1.8c-3.9-.6-7.3-4-7.9-7.9z" fill="#fff"/></svg>
        (555) 214-3380
      </li>
      <li>
        <svg viewBox="0 0 24 24" aria-hidden="true"><circle cx="12" cy="12" r="12" fill="#1c1c1c"/><rect x="8.5" y="6" width="7" height="4" fill="#fff"/><rect x="6" y="10" width="12" height="5" rx="1" fill="#fff"/><rect x="8.5" y="13.5" width="7" height="4.5" fill="#fff" stroke="#1c1c1c" stroke-width="1"/></svg>
        (555) 214-3381
      </li>
      <li>
        <svg viewBox="0 0 24 24" aria-hidden="true"><circle cx="12" cy="12" r="12" fill="#1c1c1c"/><rect x="6.5" y="8" width="11" height="8" fill="#fff"/><path d="M6.5 8l5.5 4.5L17.5 8" fill="none" stroke="#1c1c1c" stroke-width="1.2"/></svg>
        <span class="small-caps">olindqvist@lawbrtw.com</span>
      </li>
      <li>
        <svg viewBox="0 0 24 24" aria-hidden="true"><circle cx="12" cy="12" r="12" fill="#1c1c1c"/><circle cx="12" cy="12" r="5.5" fill="none" stroke="#fff" stroke-width="1.3"/><ellipse cx="12" cy="12" rx="2.3" ry="5.5" fill="none" stroke="#fff" stroke-width="1.1"/><path d="M6.5 12h11" stroke="#fff" stroke-width="1.1"/></svg>
        <span class="small-caps">www.lawbrtw.com</span>
      </li>
    </ul>

    <address class="address" style="font-style:normal">
      2740 Alder Court, Suite B<br>
      Fairhaven, CA 90412
    </address>
  </div>
</body>
</html>
```